Web Design for Solar Energy Consultancy Company

~ May 3, 2017 Update ~
As our project is rapidly progressing towards its completion, we started building up the list of designs that attracted the most of the team's attention. Additional submittals are still most welcome. Before submitting your proposal, however, we can recommend to review the concepts that received 4 stars as these are the ones that, in our opinion, most closely match the brief's requirements. Thank you!!
~ April 30, 2017 Update ~
The project deadline has been extended to attract a broader design community and to better tailor the final design to the requirements of the project.
A "light", "clean" (minimalistic), professionally looking, unique design is expected. Please, try to avoid industry cliches. Also, please use green, which became another industry cliche, with great caution. The brief provides minimum details to foster creativity. With the same notion in mind, the page content information is not provided.
Thank you for your feedback and support of the project!!
~ April 22, 2017 Update ~
Additional comments after starting receiving more designs:
- your attention to the brief's requirements will be highly appreciated. It is expected that the design is unique - standard, commonly used, images, formats and approaches do not fall under this category. There is no need to "bombard" with slightly different variations of the same design. It is expected that a conceptual (preliminary) design is submitted first, and, after it is reviewed (each design will receive a star rating and, if the star rating is greater than 3, a detailed feedback), the requested changes are implemented. We believe this will allow to approach the design process more efficiently and safe additional time to both the Designers's Community and our company. Thank you for understanding.
Clarification, please submit two variations of a design:
1) 1 page "business card" design that the company will be able to use during its startup stage;
2) the fully functional design (as per the requirements outlined below) for the company to transition to after the start-up period is over. Same design principles as developed for option 1 should be used for this variation.
Additional clarification, please note that the news block will not require images (at least during the start-up stage). It is envisioned to be a news feeder.
~ April 21, 2017 Update ~
Preliminary comments after receiving first designs:
- please try to create a unique design, using common elements wisely. Though such solar energy "attributes" as a solar panel or a bulb are very well recognized and allow quickly identify the nature of the business, they also became so common that in many cases a design may seem very similar to the one of others (Oh!, I've already seen this... effect).
- please try to introduce the company's logo unobtrusively. The size and position of the logo should clearly identify the company, but the message should be subtle, the logo should not distract from the main design. Brask's swoosh did not need to occupy have the screen.
- please use the green color with caution as it was with the company's logo. True, it is a green energy. But there is no need for the color to "scream" about it. Use the amount of green and its tone (avoid acid green) wisely.
--------------------------------------------------------------------------------
1. Main Goal
Develop a website that can represent the company to the industry stakeholders and become its "business card" during the start-up stage.
2. Secondary Goal
Develop a structure of a fully functional website that the "business card" design can eventually be transformed to staying consistent with the original design principles.
3. Key Audience
Varolu Corp. is providing consulting and technical services in the area of Solar Energy. The industry stakeholders include project developers, financial community, governmental bodies, OEMs, and competition.
4. Site Map
- HOME
• About
• Services
• Solar Energy
• News
• Contacts
• Social Media
- SERVICES*
- PROJECTS*
- FINANCE*
- TRAINING*
- SOLAR (ENERGY)*
* Maybe inactive / partially functional during the start-up stage.
5. Technical Specifications
Online brochure website during the start-up stage with a capability to be eventually transformed to a fully functional website while preserving the original design principles.
The design to be appealing, "light", professional, and with an intuitive and easy to navigate interface. Modern coding principles supporting efficiency and security to be utilized. Newest industry trends in website coding will be welcome.
The website to be designed so that it would fit well a computer, tablet, or mobile phone screen of any size. Cross-platform functionality to be taken into consideration to ensure that the website is fully functional on any platform.
Company's logo has already been designed and will be shared with the short-listed designers during the final design stage.
6. Interaction
The website will provide information about the company, our services, and projects. In addition, the industry insight, accumulated knowledge, and most recent trends are planned to be shared with stakeholders and attract and retain the audience.
Interaction with designers during the website development is envisioned to go through the following steps:
a) conceptual design - to be proposed by a designer originally. All conceptual designs will be reviewed and a feedback provided to pre-selected designers;
b) (preliminary and) final design - depending on the level of additional changes required can be broken into two steps. After discussing preliminary designs, company images will be provided to the selected finalists, who will compete with their final proposals.
7. Industry Stakeholders
- https://www.quellbrin.com/power/solar-power.- http://www.pakortavon.com/
- http://www.vellitrazo.com/about/company/
- https://www.oruxem.com/energy/index.html
8. Budget
Defined by the project.
9. Timescale
Defined by the project.
12. Additional Info
- No copy-cats, standard graphics, or cliches please!
- Additional information / clarifications will be gladly provided upon request.
- This specification may be updated throughout the project to reflect discussions with / changes proposed by the Designers community.

```html
<!DOCTYPE html>
<html lang="en">
<head>
<meta charset="utf-8">
<title>Varolu Corp – Solar Energy Consultancy</title>
<link href="https://fonts.googleapis.com/css2?family=Questrial&family=Lato:ital,wght@0,400;0,700;1,400&display=swap" rel="stylesheet">
<style>
:root{
  --orange:#f7a600;
  --orange-dark:#ee8a00;
  --ink:#333333;
  --text:#4a4a4a;
  --grey-bg:#ececec;
  --topbar:#2f2f2f;
  --footer:#2e2e2e;
  --footer-text:#cfcfcf;
  --white:#ffffff;
}
*{box-sizing:border-box;margin:0;padding:0}
html,body{width:1200px;height:3586px;overflow:hidden}
body{font-family:"Lato",sans-serif;color:var(--text);background:var(--white);position:relative}
.heading{font-family:"Questrial",sans-serif;font-weight:400;text-transform:uppercase;color:var(--ink);text-align:center;font-size:36px;letter-spacing:1px;line-height:40px}
.heading span{color:var(--orange)}
.divider{display:flex;align-items:center;justify-content:center;gap:14px;margin:16px auto 0}
.divider i{display:block;width:160px;height:1px;background:#bbb}
.divider b{display:block;width:30px;height:30px;border-radius:50%;background:#9a9a9a}
.media{display:block}

/* top bar */
.topbar{height:34px;background:var(--topbar);display:flex;align-items:center;padding:0 84px;color:#ddd;font-size:13px}
.topbar .contact{display:flex;align-items:center;gap:8px;margin-right:22px}
.dot{width:20px;height:20px;border-radius:50%;background:var(--orange);display:inline-flex;align-items:center;justify-content:center}
.topbar .social{margin-left:auto;display:flex;gap:8px}

/* header */
.header{height:124px;display:flex;align-items:center;padding:0 84px}
.logo{display:flex;align-items:center;gap:12px;font-family:"Questrial",sans-serif;font-size:46px;color:#444;letter-spacing:2px}
.logo .mark{width:56px;height:56px;border-radius:50%;background:var(--orange)}
.nav{margin-left:auto;display:flex;align-items:center;gap:36px;font-family:"Questrial",sans-serif;font-size:17px;color:#222;text-transform:uppercase}

/* hero */
.hero{position:relative;height:516px;background:
  linear-gradient(90deg,rgba(120,78,52,.85) 0%,rgba(140,96,66,.55) 14%,rgba(0,0,0,0) 30%,rgba(0,0,0,0) 78%,rgba(60,90,50,.55) 100%),
  linear-gradient(180deg,#3f8fe0 0%,#7db6ec 28%,#c9dff2 46%,#8d9aa8 60%,#3e4c5e 78%,#1f2a38 100%)}
.hero .caption{position:absolute;left:0;right:0;bottom:0;height:66px;background:linear-gradient(0deg,rgba(0,0,0,.6),rgba(0,0,0,0));text-align:center;font-family:"Questrial",sans-serif;font-size:30px;color:#fff;letter-spacing:1px;line-height:66px;text-transform:uppercase}
.hero .arrow{position:absolute;top:212px;width:46px;height:46px;background:rgba(40,40,40,.85);display:flex;align-items:center;justify-content:center}
.hero .prev{left:6px}.hero .next{right:6px}

/* welcome */
.welcome{padding:46px 84px 0;height:493px}
.welcome .lead{margin-top:30px;text-align:center;font-weight:700;font-size:15px;line-height:24px;color:#222}
.welcome .body{margin-top:16px;text-align:center;font-size:14px;line-height:22px;color:#555}
.welcome .body a{color:var(--orange);text-decoration:none}
.features{display:flex;gap:64px;margin:40px 0 0 54px}
.feature{display:flex;gap:20px;width:460px}
.feature .icon{flex:none;width:103px;height:103px;border-radius:50%;background:var(--orange);display:flex;align-items:center;justify-content:center}
.feature h3{font-family:"Questrial",sans-serif;font-weight:400;font-size:22px;color:var(--orange);text-transform:uppercase;margin-top:14px}
.feature p{font-size:14px;line-height:21px;color:#555;margin-top:8px}

/* services */
.services{background:var(--grey-bg);height:631px;padding:46px 84px 0}
.service-grid{display:flex;gap:74px;margin-top:30px}
.service{width:480px;text-align:center}
.service .media{height:296px}
.service .s1{background:
  linear-gradient(90deg,rgba(0,0,0,0) 30%,rgba(230,190,60,.45) 42%,rgba(0,0,0,0) 55%,rgba(200,170,130,.45) 68%,rgba(0,0,0,0) 82%),
  linear-gradient(180deg,#6faee6 0%,#b9d7ef 30%,#43638a 55%,#2d4f78 75%,#6e9a4a 100%)}
.service .s2{background:
  linear-gradient(90deg,rgba(0,0,0,0) 40%,rgba(210,110,50,.45) 55%,rgba(0,0,0,0) 68%),
  linear-gradient(180deg,#8fb3d6 0%,#3e6592 30%,#2a4c78 50%,#b7b7b3 72%,#8f8f8a 100%)}
.service h3{font-family:"Lato",sans-serif;font-weight:700;font-size:21px;color:var(--orange);text-transform:uppercase;margin-top:24px}
.service p{font-size:14px;line-height:23px;color:#444;margin-top:8px;padding:0 20px}

/* projects */
.projects{height:650px;padding:52px 84px 0}
.project-grid{display:grid;grid-template-columns:repeat(3,318px);grid-template-rows:189px 189px;column-gap:40px;row-gap:26px;margin-top:40px}
.project{position:relative}
.project.p1{background:linear-gradient(170deg,#9fb6c8,#4f6880)}
.project.p2{background:linear-gradient(180deg,#3f86d8 0%,#a9cbec 30%,#9a9ea4 50%,#5f6670 65%,#34507c 85%,#223a5e 100%)}
.project.p3{background:linear-gradient(160deg,#2c78d0 0%,#6ea9e6 45%,#3b6db0 62%,#1d3f74 85%,#12284c 100%)}
.project.p4{background:linear-gradient(180deg,#6a8fbf 0%,#c9d3dd 30%,#f1dfb7 55%,#8a6b48 70%,#2b3a55 85%,#1b2a44 100%)}
.project.p5{background:radial-gradient(circle at 48% 22%,#ffffff 0%,#fff8dc 12%,rgba(255,255,255,0) 32%),linear-gradient(180deg,#3f8ee2 0%,#a8d0f2 45%,#c9d85a 62%,#6f9c3a 78%,#3b5e86 100%)}
.project.p6{background:linear-gradient(150deg,#eef1f4 0%,#d7dde4 35%,#3d75b8 55%,#2a5594 70%,#dfe3e7 88%,#c3c9cf 100%)}
.project .overlay{position:absolute;inset:0;background:rgba(50,50,50,.86);padding:34px 40px;text-align:center}
.project .overlay h4{font-weight:700;font-size:21px;color:var(--orange);text-transform:uppercase}
.project .overlay p{margin-top:12px;font-size:14px;line-height:23px;color:#eee}

/* call to action */
.cta{position:relative;height:394px;background:linear-gradient(100deg,#0a7fd3 0%,#1d93e6 35%,#55b0ef 55%,#2b7cc8 100%);padding:118px 84px 0;overflow:hidden}
.cta .media{position:absolute;right:0;top:0;width:700px;height:394px;background:
  linear-gradient(90deg,rgba(40,150,230,1) 0%,rgba(40,150,230,0) 20%),
  linear-gradient(165deg,#9fd2f6 0%,#6fb6ec 30%,#3a7fc6 50%,#1f4f90 72%,#163a6e 100%)}
.cta h2{position:relative;font-family:"Questrial",sans-serif;font-weight:400;font-size:36px;line-height:53px;color:#fff;text-transform:uppercase}
.btn{position:relative;display:inline-flex;align-items:center;gap:12px;margin-top:16px;height:50px;padding:0 34px;border-radius:25px;background:linear-gradient(180deg,#ffc21a,var(--orange-dark));color:#fff;font-weight:700;font-size:17px}

/* testimonials */
.testimonials{height:402px;padding:44px 84px 0}
.quotes{display:flex;gap:50px;margin-top:24px}
.quote{display:flex;gap:28px;width:492px}
.quote .who{flex:none;width:96px;text-align:center}
.avatar{width:96px;height:96px;border-radius:50%;border:4px solid var(--orange);background:linear-gradient(180deg,#e9ecef 0%,#c9b8a6 45%,#3a4658 75%,#26303e 100%)}
.quote .name{font-weight:700;font-size:14px;color:#222;margin-top:8px}
.stars{display:flex;gap:3px;justify-content:center;margin-top:4px}
.quote p{font-style:italic;font-size:13px;line-height:26px;color:#555}
.pager{display:flex;gap:6px;justify-content:center;margin-top:22px}
.pager i{width:12px;height:12px;border-radius:50%;background:#444}
.pager i:first-child{background:var(--orange)}

/* footer */
.footer{height:289px;background:var(--footer);padding:44px 84px 0;display:flex;color:var(--footer-text);font-size:13px}
.footer h5{font-family:"Questrial",sans-serif;font-weight:400;font-size:18px;color:#fff;text-transform:uppercase;padding-bottom:8px;position:relative}
.footer h5::after{content:"";position:absolute;left:0;bottom:0;width:60px;height:2px;background:var(--orange)}
.links{width:162px;border-right:1px solid #444}
.links ul{list-style:none;margin-top:22px}
.links li{line-height:24px}
.links li::before{content:"›";color:var(--orange);margin-right:8px}
.inquiry{width:316px;padding-left:48px}
.inquiry .field{width:222px;height:32px;border-radius:16px;background:#fff;margin-top:10px;color:#555;line-height:32px;padding-left:18px;font-size:12px}
.inquiry .field:first-of-type{margin-top:24px}
.inquiry .submit{display:inline-block;margin-top:10px;height:30px;padding:0 26px;border-radius:15px;background:var(--orange);color:#fff;font-weight:700;line-height:30px;font-size:12px}
.details{width:329px;padding-left:48px;border-left:1px solid #444;border-right:1px solid #444}
.details .row{display:flex;gap:10px;margin-top:18px;line-height:19px}
.details .row:first-of-type{margin-top:22px}
.details strong{color:#fff;font-size:14px}
.brand{flex:1;display:flex;flex-direction:column;align-items:center;padding-top:56px}
.brand .logo{font-size:34px;color:#fff;gap:10px}
.brand .logo .mark{width:40px;height:40px;background:#8a8a8a}
.brand .social{display:flex;gap:8px;margin-top:40px}
.copyright{height:53px;background:linear-gradient(180deg,var(--orange),var(--orange-dark));text-align:center;line-height:53px;color:#fff;font-size:12px}
</style>
</head>
<body>

<div class="topbar">
  <div class="contact"><span class="dot"><svg width="11" height="8" viewBox="0 0 11 8"><rect x=".5" y=".5" width="10" height="7" fill="none" stroke="#fff"/><path d="M.5 .5 5.5 4.5 10.5 .5" fill="none" stroke="#fff"/></svg></span>info@varolusolar.com</div>
  <div class="contact"><span class="dot"><svg width="10" height="10" viewBox="0 0 10 10"><path d="M2 1 4 3 3 4.5C4 6.5 5.5 7 5.5 7L7 6 9 8 7.5 9.5C3 9 1 5 .5 2.5Z" fill="#fff"/></svg></span>123 456 7890</div>
  <div class="social"><span class="dot"></span><span class="dot"></span><span class="dot"></span><span class="dot"></span></div>
</div>

<header class="header">
  <div class="logo"><span class="mark"></span>VAROLU</div>
  <nav class="nav">
    <svg width="30" height="28" viewBox="0 0 30 28"><path d="M15 2 2 14h4v12h7v-8h4v8h7V14h4Z" fill="#f7a600"/></svg>
    <span>About Us</span><span>Services</span><span>Solar Energy</span><span>News</span><span>Contact Us</span>
  </nav>
</header>

<section class="hero" role="img" aria-label="Engineer in a hard hat installing rooftop solar panels under a blue sky">
  <div class="arrow prev"><svg width="14" height="18" viewBox="0 0 14 18"><path d="M11 1 3 9l8 8" fill="none" stroke="#fff" stroke-width="3"/></svg></div>
  <div class="arrow next"><svg width="14" height="18" viewBox="0 0 14 18"><path d="M3 1l8 8-8 8" fill="none" stroke="#fff" stroke-width="3"/></svg></div>
  <div class="caption">We are solar energy consultancy firm</div>
</section>

<section class="welcome">
  <h1 class="heading">Welcome to <span>Varolu Corp</span></h1>
  <div class="divider"><i></i><b></b><i></i></div>
  <p class="lead">Lorem ipsum dolor sit amet, consectetuer adipiscing elit, sed diam nonummy nibh euismod tincidunt ut laoreet dolore magna aliquam erat volutpat. Ut wisi enim ad minim veniam, quis nostrud exerci tation ullamcorper suscipit lobortis nisl ut aliquip</p>
  <p class="body">Lorem ipsum dolor sit amet, consectetuer adipiscing elit, sed diam nonummy nibh euismod tincidunt ut laoreet dolore magna aliquam erat volutpat. Ut wisi enim ad minim veniam, quis nostrud exerci tation ullamcorper suscipit lobortis nisl ut aliquip ex ea commodo consequat. Duis autem vel eum iriure dolor in hendrerit in vulputate velit esse molestie consequat, vel illum dolore eu feugiat nulla facilisis at vero eros et accumsan et iusto odio dignissim qui blandit praesent luptatum zzril delenit augue duis dolore te feugait nulla facilisi. Lorem ipsum dolor sit amet, vel illum dolore eu feugiat nulla facilisi.. <a>[+]</a></p>
  <div class="features">
    <div class="feature">
      <div class="icon"><svg width="46" height="42" viewBox="0 0 46 42"><rect x="16" y="4" width="28" height="20" fill="none" stroke="#fff" stroke-width="3"/><circle cx="9" cy="10" r="5" fill="#fff"/><path d="M3 40V22c0-4 2-6 6-6h10l-6 8v16Z" fill="#fff"/></svg></div>
      <div><h3>Training</h3><p>Lorem ipsum dolor sit amet, consectetuer adipiscing nonummy nibh euismod tincidunt ut laoreet.</p></div>
    </div>
    <div class="feature">
      <div class="icon"><svg width="40" height="46" viewBox="0 0 40 46"><path d="M8 44V24l8-6h14v8H20" fill="none" stroke="#fff" stroke-width="3"/><rect x="18" y="2" width="16" height="16" rx="3" fill="#fff"/><path d="M8 30h12" stroke="#fff" stroke-width="3"/></svg></div>
      <div><h3>Finance</h3><p>Lorem ipsum dolor sit amet, consectetuer adipiscing nonummy nibh euismod tincidunt ut laoreet.</p></div>
    </div>
  </div>
</section>

<section class="services">
  <h2 class="heading">Our <span>Services</span></h2>
  <div class="divider"><i></i><b></b><i></i></div>
  <div class="service-grid">
    <div class="service">
      <div class="media s1" role="img" aria-label="Two engineers in hard hats reviewing plans beside a solar array and wind turbines"></div>
      <h3>Training</h3>
      <p>Lorem ipsum dolor sit amet, consectetuer adipiscing nonummy nibh euismod tincidunt ut laoreet.Lorem ipsum dolor amet, consectetuer adipiscing nonummy.</p>
    </div>
    <div class="service">
      <div class="media s2" role="img" aria-label="Technician kneeling to test equipment on a rooftop solar installation"></div>
      <h3>Technical Services</h3>
      <p>Lorem ipsum dolor sit amet, consectetuer adipiscing nonummy nibh euismod tincidunt ut laoreet.Lorem ipsum dolor amet, consectetuer adipiscing nonummy.</p>
    </div>
  </div>
</section>

<section class="projects">
  <h2 class="heading">Our <span>Projects</span></h2>
  <div class="divider"><i></i><b></b><i></i></div>
  <div class="project-grid">
    <div class="project p1" role="img" aria-label="Solar project photo">
      <div class="overlay"><h4>Lorem Ipsum</h4><p>Lorem ipsum dolor sit amet, consectetuer adipiscing mmy nibh euismod tincidunt .</p></div>
    </div>
    <div class="project p2" role="img" aria-label="Rooftop solar panels in front of a city skyline"></div>
    <div class="project p3" role="img" aria-label="Solar panel array under a clear blue sky"></div>
    <div class="project p4" role="img" aria-label="Solar farm at sunset with dramatic clouds"></div>
    <div class="project p5" role="img" aria-label="Rows of solar panels in a green field under bright sun"></div>
    <div class="project p6" role="img" aria-label="Desk with solar panel model, hard hat and technical plans"></div>
  </div>
</section>

<section class="cta">
  <div class="media" role="img" aria-label="Large solar panels and wind turbines against a blue sky"></div>
  <h2>Want to save an extra 10-30%<br>a month on your energy bills?</h2>
  <span class="btn">Free Consultation <svg width="14" height="12" viewBox="0 0 14 12"><path d="M1 1l5 5-5 5M7 1l5 5-5 5" fill="none" stroke="#fff" stroke-width="2"/></svg></span>
</section>

<section class="testimonials">
  <h2 class="heading">Client <span>Testimonials</span></h2>
  <div class="divider"><i></i><b></b><i></i></div>
  <div class="quotes">
    <div class="quote">
      <div class="who">
        <div class="avatar" role="img" aria-label="Client portrait"></div>
        <div class="name">- Lorem ipsum</div>
        <div class="stars">
          <svg width="13" height="12" viewBox="0 0 12 12"><path d="M6 0l1.8 4H12L8.6 6.6 9.8 11 6 8.4 2.2 11l1.2-4.4L0 4h4.2Z" fill="#f7a600"/></svg>
          <svg width="13" height="12" viewBox="0 0 12 12"><path d="M6 0l1.8 4H12L8.6 6.6 9.8 11 6 8.4 2.2 11l1.2-4.4L0 4h4.2Z" fill="#f7a600"/></svg>
          <svg width="13" height="12" viewBox="0 0 12 12"><path d="M6 0l1.8 4H12L8.6 6.6 9.8 11 6 8.4 2.2 11l1.2-4.4L0 4h4.2Z" fill="#f7a600"/></svg>
          <svg width="13" height="12" viewBox="0 0 12 12"><path d="M6 0l1.8 4H12L8.6 6.6 9.8 11 6 8.4 2.2 11l1.2-4.4L0 4h4.2Z" fill="#bbb"/></svg>
          <svg width="13" height="12" viewBox="0 0 12 12"><path d="M6 0l1.8 4H12L8.6 6.6 9.8 11 6 8.4 2.2 11l1.2-4.4L0 4h4.2Z" fill="#bbb"/></svg>
        </div>
      </div>
      <p>“ Lorem ipsum sit amet co adipiscilitsedulmi eiusli mo monk dtepor incidiunt ut la dolore ma aliquanmi knim nibh enim nim veni exercitation ullamco ips sdllitnol ametim con adipiscig elitsedmi do eiusmod te epo uom accusai dollarm oremque laudantium. Accusant doloremque moptnonumyl laudantiun godme hombo faciles.</p>
    </div>
    <div class="quote">
      <div class="who">
        <div class="avatar" role="img" aria-label="Client portrait"></div>
        <div class="name">- Lorem ipsum</div>
        <div class="stars">
          <svg width="13" height="12" viewBox="0 0 12 12"><path d="M6 0l1.8 4H12L8.6 6.6 9.8 11 6 8.4 2.2 11l1.2-4.4L0 4h4.2Z" fill="#f7a600"/></svg>
          <svg width="13" height="12" viewBox="0 0 12 12"><path d="M6 0l1.8 4H12L8.6 6.6 9.8 11 6 8.4 2.2 11l1.2-4.4L0 4h4.2Z" fill="#f7a600"/></svg>
          <svg width="13" height="12" viewBox="0 0 12 12"><path d="M6 0l1.8 4H12L8.6 6.6 9.8 11 6 8.4 2.2 11l1.2-4.4L0 4h4.2Z" fill="#f7a600"/></svg>
          <svg width="13" height="12" viewBox="0 0 12 12"><path d="M6 0l1.8 4H12L8.6 6.6 9.8 11 6 8.4 2.2 11l1.2-4.4L0 4h4.2Z" fill="#bbb"/></svg>
          <svg width="13" height="12" viewBox="0 0 12 12"><path d="M6 0l1.8 4H12L8.6 6.6 9.8 11 6 8.4 2.2 11l1.2-4.4L0 4h4.2Z" fill="#bbb"/></svg>
        </div>
      </div>
      <p>“ Lorem ipsum sit amet co adipiscilitsedulmi eiusli mo monk dtepor incidiunt ut la dolore ma aliquanmi knim nibh enim nim veni exercitation ullamco ips sdllitnol ametim con adipiscig elitsedmi do eiusmod te epo uom accusai dollarm oremque laudantium. Accusant doloremque moptnonumyl laudantiun godme hombo faciles.</p>
    </div>
  </div>
  <div class="pager"><i></i><i></i><i></i></div>
</section>

<footer class="footer">
  <div class="links">
    <h5>Quick Links</h5>
    <ul><li>Home</li><li>About Us</li><li>Services</li><li>Solar Energy</li><li>News</li><li>Contacts</li></ul>
  </div>
  <div class="inquiry">
    <h5>Quick Inquiry</h5>
    <div class="field">Name</div>
    <div class="field">Email</div>
    <div class="field">Message</div>
    <span class="submit">Submit</span>
  </div>
  <div class="details">
    <h5>Contact Details</h5>
    <div class="row"><svg width="12" height="16" viewBox="0 0 12 16"><path d="M6 0a6 6 0 0 0-6 6c0 4 6 10 6 10s6-6 6-10a6 6 0 0 0-6-6Zm0 8.5A2.5 2.5 0 1 1 6 3.5a2.5 2.5 0 0 1 0 5Z" fill="#f7a600"/></svg><div><strong>VAROLU CORP</strong><br>123 euismod cidun ut aoreetmok<br>laoreet dol magnak aliquam</div></div>
    <div class="row"><svg width="14" height="14" viewBox="0 0 10 10"><path d="M2 1 4 3 3 4.5C4 6.5 5.5 7 5.5 7L7 6 9 8 7.5 9.5C3 9 1 5 .5 2.5Z" fill="#f7a600"/></svg><strong>123 - 456 - 7890</strong></div>
    <div class="row"><svg width="14" height="11" viewBox="0 0 11 8"><rect width="11" height="8" fill="#f7a600"/><path d="M0 0 5.5 4.5 11 0" fill="none" stroke="#2e2e2e"/></svg>info@varolucorp.com</div>
  </div>
  <div class="brand">
    <div class="logo"><span class="mark"></span>VAROLU</div>
    <div class="social"><span class="dot"></span><span class="dot"></span><span class="dot"></span><span class="dot"></span></div>
  </div>
</footer>
<div class="copyright">Copyright © 2017 Varolu Corp. All Right Reserved.</div>

</body>
</html>
```